Residential Construction Business - Site Signage

I need a design made for a site fence banner. We have a logo and branding so the design would need to be aligned with this. It would need to be made to specific size ratio so that it can be sent to the maker for production.
ratio : 4600 wide x 1700 high
The design should feature our website and also the slogan
"STAY HOME, RE-INVENT"

Target Market(s)

potential clients

Industry/Entity Type

construction

Font styles to use
Other font styles liked:
• to match branding

Colors
0054AA
0677BA
7BADD7
CADEEF
E8F1F8

Requirements
Must have
• www.velmbuild.com.au Majority of the sign is our brand logo
Nice to have
• Majority of the sign is our brand logo
Should not have
• colors and themes that arent brand relevant

```html
<!DOCTYPE html>
<html lang="en">
<head>
<meta charset="utf-8">
<title>Velmbuild – Site Fence Banner</title>
<link rel="stylesheet" href="https://fonts.googleapis.com/css2?family=Montserrat:wght@400;500;800&display=swap">
<style>
  :root {
    --brand-navy: #023e5f;
    --paper: #fdfdfd;
    --page: #ffffff;
  }
  * { margin: 0; padding: 0; box-sizing: border-box; }
  html, body {
    width: 1200px;
    height: 1000px;
    overflow: hidden;
    background: var(--page);
  }
  .banner {
    position: absolute;
    left: 50px;
    top: 297px;
    width: 1100px;
    height: 406px;
    background: var(--paper);
    overflow: hidden;
    font-family: "Montserrat", sans-serif;
  }
  .banner-shapes {
    position: absolute;
    inset: 0;
    width: 100%;
    height: 100%;
  }
  .banner-shapes path { fill: var(--brand-navy); }
  .brand-name {
    position: absolute;
    left: 300px;
    top: 180px;
    font-size: 42px;
    font-weight: 500;
    letter-spacing: 0.3em;
    line-height: 1;
    color: var(--brand-navy);
    white-space: nowrap;
  }
  .slogan {
    position: absolute;
    left: 747px;
    top: 256px;
    font-size: 42px;
    font-weight: 800;
    line-height: 49px;
    color: var(--paper);
    text-transform: uppercase;
    white-space: nowrap;
  }
  .slogan-rule {
    position: absolute;
    left: 749px;
    top: 357px;
    width: 289px;
    height: 1.5px;
    background: var(--paper);
  }
  .website {
    position: absolute;
    left: 749px;
    top: 368px;
    font-size: 12.5px;
    font-weight: 400;
    letter-spacing: 0.24em;
    color: var(--paper);
    text-transform: uppercase;
    white-space: nowrap;
  }
</style>
</head>
<body>
  <section class="banner" aria-label="Velmbuild site fence banner">
    <svg class="banner-shapes" viewBox="0 0 1100 406" aria-hidden="true">
      <path class="chevron-band" d="M0 50 H417 L292 175 Q268 203 292 231 L417 356 H0 Z"/>
      <path class="corner-wedge" d="M941 0 H1100 V406 H539 Q548 390 563 378 Z"/>
    </svg>
    <h1 class="brand-name">VELMBUILD</h1>
    <p class="slogan">Stay home,<br>Re-invent</p>
    <div class="slogan-rule"></div>
    <p class="website">www.velmbuild.com.au</p>
  </section>
</body>
</html>
```